Rocket business card

Modern business card design, use of color is good with clean space too.

Things to include on card:

Quote: I add fuel to your optometry practice

- Eyewear Sales
- Admin Duties
- Revenue Collection
- Leadership
- Tech Adoption
- COGS Reduction
- Product Sourcing
-Medical Growth

Dalton Vessey, CEO
Glint Harbor
Text Me! 847-302-1964
dalton@glintharbor.example

```html
<!DOCTYPE html>
<html lang="en">
<head>
<meta charset="utf-8">
<title>Glint Harbor — Business Card</title>
<link href="https://fonts.googleapis.com/css2?family=Lato:wght@400;700;900&display=swap" rel="stylesheet">
<style>
  :root {
    --bg: #1c1c1e;
    --card: #ffffff;
    --red: #ee2426;
    --rust: #e2502e;
    --orange: #f08a24;
    --ink: #2a1414;
    --pill: #1b1b1b;
    --pill-text: #ffffff;
  }
  * { margin: 0; padding: 0; box-sizing: border-box; }
  html, body { width: 1200px; height: 900px; overflow: hidden; background: var(--bg); }
  body { font-family: "Lato", sans-serif; position: relative; }

  .card {
    position: absolute;
    left: 250px;
    width: 700px;
    height: 400px;
    background: var(--card);
    overflow: hidden;
    box-shadow: 0 12px 30px rgba(0,0,0,.5);
  }
  .card--front { top: 35px; }
  .card--back { top: 465px; }
  .card svg.bands { position: absolute; inset: 0; }

  .holder {
    position: absolute;
    left: 46px;
    top: 52px;
    color: var(--ink);
  }
  .holder__name { font-weight: 900; font-size: 29px; line-height: 1.1; }
  .holder__company { font-weight: 900; font-size: 24px; margin-top: 6px; }
  .duties { list-style: none; margin-top: 12px; padding-left: 24px; }
  .duties li { font-size: 17px; line-height: 1.28; }

  .pill {
    position: absolute;
    background: var(--pill);
    color: var(--pill-text);
    border-radius: 20px;
    font-size: 17px;
    padding: 6px 26px;
    white-space: nowrap;
  }
  .pill--email { left: 36px; bottom: 22px; }
  .pill--phone { right: 26px; bottom: 54px; }

  .brand {
    position: absolute;
    display: flex;
    flex-direction: column;
    align-items: center;
    color: var(--ink);
    font-weight: 400;
    text-transform: uppercase;
    white-space: nowrap;
  }
  .brand__dot { border-radius: 50%; background: var(--orange); flex: none; }
  .brand--front { left: 440px; top: 62px; width: 240px; gap: 14px; font-size: 24px; letter-spacing: 2px; }
  .brand--front .brand__dot { width: 52px; height: 52px; }
  .brand--back { left: 100px; top: 120px; width: 300px; gap: 18px; font-size: 32px; letter-spacing: 2px; }
  .brand--back .brand__dot { width: 72px; height: 72px; }
</style>
</head>
<body>

<section class="card card--front" aria-label="Business card front">
  <svg class="bands" width="700" height="400" viewBox="0 0 700 400" aria-hidden="true">
    <circle cx="-60" cy="380" r="502" fill="var(--orange)"/>
    <circle cx="-60" cy="380" r="490" fill="var(--rust)"/>
    <circle cx="-60" cy="380" r="470" fill="var(--red)"/>
  </svg>

  <div class="holder">
    <p class="holder__name">Dalton Vessey, CEO</p>
    <p class="holder__company">Glint Harbor</p>
    <ul class="duties">
      <li>-Eyewear sales</li>
      <li>-Admin Duties</li>
      <li>-Leadership</li>
      <li>-Tech Adoption</li>
      <li>-Cogs Reduction</li>
      <li>-Product Sourcing</li>
      <li>-Medical Growth</li>
    </ul>
  </div>

  <p class="pill pill--email">dalton@glintharbor.example</p>

  <div class="brand brand--front">
    <span class="brand__dot"></span>
    <span class="brand__name">Glint Harbor</span>
  </div>

  <p class="pill pill--phone">text me:+847-302-1964</p>
</section>

<section class="card card--back" aria-label="Business card back">
  <svg class="bands" width="700" height="400" viewBox="0 0 700 400" aria-hidden="true">
    <circle cx="760" cy="80" r="352" fill="var(--orange)"/>
    <circle cx="760" cy="80" r="340" fill="var(--rust)"/>
    <circle cx="760" cy="80" r="320" fill="var(--red)"/>
  </svg>

  <div class="brand brand--back">
    <span class="brand__dot"></span>
    <span class="brand__name">Glint Harbor</span>
  </div>
</section>

</body>
</html>
```